Web Site for Strategy and Technology Consulting Company

We are looking for a website design that engages potential customers to understand our services and contact us. In this contest, we are looking for a homepage design, but the winning designer will be favored for the design of some of the more complicated interior pages of the site. An additional contest (or contests) for these pages will be added soon.

PLATROM AND RESPONSIVE DESIGN
The site will be implemented in WordPress using the Elementor page builder.
We are looking for a design that will look good on phones are well as laptop browsers.

UPLOADED FILES INCLUDE:
1a A wireframe of the homepage we are looking for. The Uploaded PDF also includes a draft of the text proposed for the homepage. Designers are free to go beyond the wireframe, but all elements of the wireframe should be included.
1b A Word document with the draft text of the homepage.
2a-d The Corvalin logo. Two versions are included – a dark version which works well against a light background, and a light version which works well against a dark background.
3 The Corvalin color palette with HEX and RGB values. Designers are not limited to this palette, but colors should be complementary.
4 A draft of the homepage menu
5 Service sheets with information on the services we provide

MORE ABOUT CORVALIN
Corvalin is a consulting company focused on transforming businesses through software. Our tagline, “Transformation Delivered,” recognizes the gap business often have between business transformation and the software they end up with. By listening to our customers and understanding their vision and where they are, we help get our customers where they want to go.

We increase our capability by working with many consultants and partners, allowing us to provide our customers with the best people and the software that best suits them.

Industry/Entity Type

Consulting

Number of Pages Required

1 page

Font styles to use
Sans Serif

Requirements
Must have
• the content represented on the wireframe uploaded
Nice to have
• interactive features, such as roll-over icons that reveal additional information

```html
<!DOCTYPE html>
<html lang="en">
<head>
<meta charset="utf-8">
<title>Corvalin — Transformation Delivered</title>
<link href="https://fonts.googleapis.com/css2?family=Inter:wght@300;400;500;600&family=Rubik:wght@500;600&display=swap" rel="stylesheet">
<style>
:root{
  --blue:#24609a;
  --yellow:#e2b80e;
  --ink:#111318;
  --grey:#5a5f66;
  --light:#f2f6fa;
  --footer:#2b3547;
  --white:#ffffff;
  --hero-b:#8a9098;
}
*{box-sizing:border-box;margin:0;padding:0}
html,body{width:1200px;height:3232px;overflow:hidden}
body{position:relative;background:var(--white);font-family:"Inter",sans-serif;color:var(--ink)}
.abs{position:absolute}
h1,h2{font-family:"Rubik",sans-serif;font-weight:600}
.accent{color:var(--blue)}
.btn{position:absolute;display:flex;align-items:center;justify-content:center;background:var(--yellow);color:var(--ink);font-size:14px;font-weight:500;border-radius:4px}

/* hero */
.hero{position:absolute;left:0;top:0;width:1200px;height:678px;background:linear-gradient(90deg,#3c4148 0%,#555b63 45%,var(--hero-b) 100%)}
.hero-photo{position:absolute;left:560px;top:0;width:640px;height:678px;background:radial-gradient(ellipse at 55% 40%,#a9aeb3 0%,#737980 45%,rgba(80,86,94,0) 80%)}
.logo{position:absolute;font-family:"Inter",sans-serif;font-weight:300;letter-spacing:.5px;display:flex;align-items:center;gap:8px}
.logo .mark{width:12px;height:12px;border-radius:50%;background:var(--yellow)}
.nav{position:absolute;left:402px;top:34px;display:flex;gap:30px;color:var(--white);font-size:14px}
.nav span::after{content:"";display:inline-block;width:6px;height:6px;border-right:1.6px solid #fff;border-bottom:1.6px solid #fff;transform:rotate(45deg);margin-left:8px;position:relative;top:-3px}
.hero h1{position:absolute;left:60px;top:168px;font-size:52px;color:var(--white);letter-spacing:.3px}
.hero h1 .accent{color:#a8c9ec}
.hero-copy{position:absolute;left:61px;top:236px;width:630px;color:var(--white);font-size:14px;line-height:22.6px}
.checks{position:absolute;left:60px;list-style:none;color:var(--white);font-size:14px;line-height:22.6px}
.checks li{position:absolute;left:0;width:560px;padding-left:30px;white-space:nowrap}
.checks svg{position:absolute;left:0;top:3px}

/* services */
.services{position:absolute;left:0;top:678px;width:1200px;height:690px;background:var(--light)}
.sec-title{position:absolute;font-size:40px;letter-spacing:.2px}
.lead{position:absolute;left:61px;top:793px;width:760px;font-size:13.5px;line-height:22.6px;color:var(--grey)}
.card{position:absolute;top:890px;width:255px;height:389px;background:var(--white);border-top:2px solid var(--blue);box-shadow:0 2px 6px rgba(0,0,0,.05)}
.card .icon{position:absolute;left:10px;top:12px;width:70px;height:70px;border:1.5px solid var(--blue);border-radius:6px;background:var(--white);display:flex;align-items:center;justify-content:center}
.card .icon.solid{background:var(--blue)}
.card h3{position:absolute;left:96px;top:20px;font-size:16px;font-weight:600;line-height:24px}
.card p{position:absolute;left:13px;top:93px;width:210px;font-size:13.5px;line-height:22.6px;color:var(--grey)}
.card .media{position:absolute;left:8px;top:177px;width:239px;height:204px;border-radius:4px}
.card .go{position:absolute;right:17px;top:154px;width:40px;height:40px;border-radius:50%;background:#2f3a4b;display:flex;align-items:center;justify-content:center;z-index:2}
.card .go.hl{background:var(--yellow)}
.pager{position:absolute;display:flex;gap:4px}
.pager i{display:block;width:29px;height:3px;background:var(--blue)}
.pager i.on{background:var(--yellow)}

/* people */
.ghost{position:absolute;top:1425px;font-family:"Rubik",sans-serif;font-weight:600;font-size:58px;color:#ececec}
.people-band{position:absolute;left:0;top:1709px;width:267px;height:300px;background:var(--blue)}
.ring{position:absolute;left:60px;top:1502px;width:414px;height:414px;border-radius:50%;border:1px dashed #e6d27a;background:var(--white)}
.people-photo{position:absolute;left:106px;top:1548px;width:322px;height:322px;border-radius:50%;background:radial-gradient(circle at 45% 60%,#3a6fa8 0%,#7f9cb8 40%,#c9d3dc 75%)}
.people-copy{position:absolute;left:552px;width:590px;font-size:13.5px;line-height:22.6px;color:var(--grey)}
.people-list li{position:absolute;left:552px;width:560px;padding-left:36px;list-style:none;font-size:13.5px;line-height:22.6px;color:var(--grey)}
.people-list svg{position:absolute;left:0;top:4px}

/* testimonials */
.reviews{position:absolute;left:0;top:1977px;width:1200px;height:514px;background:var(--blue)}
.reviews h2{position:absolute;left:0;top:52px;width:1200px;text-align:center;font-size:38px;color:var(--white)}
.quote{position:absolute;top:2098px;width:435px;height:230px;background:var(--white);border-top:3px solid var(--yellow);border-radius:0 0 10px 10px}
.quote p{position:absolute;left:36px;top:31px;width:360px;font-size:13.5px;line-height:22.6px;color:var(--grey)}
.quote .rating{position:absolute;left:36px;top:177px;display:flex;align-items:center;gap:2px;font-size:12.5px;color:var(--ink)}
.quote .rating b{margin-left:10px;font-weight:600}
.quote .tail{position:absolute;left:50px;bottom:-20px;width:0;height:0;border-right:40px solid transparent;border-top:20px solid var(--white)}
.author{position:absolute;top:2354px;display:flex;align-items:center;gap:16px}
.avatar{width:76px;height:76px;border-radius:50%;background:linear-gradient(160deg,#d8cbb8,#8c7a66);border:3px solid var(--white)}
.author .name{font-size:16px;font-weight:600;color:var(--yellow)}
.author .co{font-size:14px;color:var(--white);margin-top:6px}
.slide-btn{position:absolute;top:2184px;width:40px;height:40px;border-radius:50%;display:flex;align-items:center;justify-content:center}

/* partners */
.partners-title{position:absolute;left:0;top:2556px;width:1200px;text-align:center;font-size:40px}
.tile{position:absolute;top:2619px;width:204px;height:146px;background:var(--light);border-radius:4px;display:flex;align-items:center;justify-content:center;gap:10px;font-size:30px;font-weight:500;color:#2c2f36}
.tile.active{background:var(--blue);color:var(--white)}
.tile .sq{width:26px;height:26px;border-radius:50%;background:var(--yellow)}

/* footer */
.footer-shape{position:absolute;left:0;top:2840px}
.footer{position:absolute;left:0;top:2905px;width:1200px;height:327px;background:var(--footer)}
.f-about{position:absolute;left:61px;top:3026px;width:240px;font-size:12.5px;line-height:20px;color:var(--white)}
.f-col h4{position:absolute;top:2982px;font-size:15px;font-weight:600;color:var(--yellow)}
.f-link{position:absolute;left:339px;font-size:12.5px;color:var(--white)}
.f-contact{position:absolute;left:644px;font-size:12.5px;line-height:21px;color:var(--white)}
.f-contact svg{position:absolute;left:-32px;top:2px}
.social{position:absolute;top:3016px;width:34px;height:34px;border-radius:50%;border:1.5px solid var(--white)}
.social.on{background:var(--yellow);border-color:var(--yellow)}
.social::after{content:"";position:absolute;left:11px;top:11px;width:9px;height:9px;border-radius:2px;border:1.5px solid var(--white)}
.copyright{position:absolute;left:0;top:3190px;width:1200px;border-top:1px solid rgba(255,255,255,.15);padding-top:14px;text-align:center;font-size:12px;color:var(--white)}
</style>
</head>
<body>

<!-- HERO -->
<section class="hero">
  <div class="hero-photo" role="img" aria-label="Photo of two smiling colleagues celebrating at a computer in a bright office"></div>
  <div class="logo" style="left:60px;top:14px;font-size:50px;color:var(--white)"><span class="mark"></span>Corvalin</div>
  <nav class="nav"><span>About Us</span><span>Services</span><span>Insights</span><span>Join Us</span></nav>
  <div class="btn" style="left:1007px;top:23px;width:133px;height:36px">Contact Us</div>
  <h1>Transformation <span class="accent">Delivered.</span></h1>
  <p class="hero-copy">We do more for our customers than implement software. We listen. We work to understand where they are in their transformation journey and where they want to go. We partner with them to clear the roadblocks that stand in their way, ensuring they reach their destination. At Corvalin, we:</p>
  <ul class="checks">
    <li style="top:336px"><svg width="18" height="18" viewBox="0 0 18 18"><path d="M3 9a6 6 0 0 1 10.5-4M15 9a6 6 0 0 1-10.5 4" fill="none" stroke="#e2b80e" stroke-width="1.6"/><path d="M6 9l2 2 4-4" fill="none" stroke="#e2b80e" stroke-width="1.6"/></svg>Focus on business value, with an emphasis on delivering value quickly.</li>
    <li style="top:363px;white-space:normal;width:490px"><svg width="18" height="18" viewBox="0 0 18 18"><path d="M3 9a6 6 0 0 1 10.5-4M15 9a6 6 0 0 1-10.5 4" fill="none" stroke="#e2b80e" stroke-width="1.6"/><path d="M6 9l2 2 4-4" fill="none" stroke="#e2b80e" stroke-width="1.6"/></svg>Meet our customers where they are without backing them up to the beginning of their journey.</li>
    <li style="top:415px"><svg width="18" height="18" viewBox="0 0 18 18"><path d="M3 9a6 6 0 0 1 10.5-4M15 9a6 6 0 0 1-10.5 4" fill="none" stroke="#e2b80e" stroke-width="1.6"/><path d="M6 9l2 2 4-4" fill="none" stroke="#e2b80e" stroke-width="1.6"/></svg>Provide a wide range of services, from strategy to product support.</li>
    <li style="top:446px"><svg width="18" height="18" viewBox="0 0 18 18"><path d="M3 9a6 6 0 0 1 10.5-4M15 9a6 6 0 0 1-10.5 4" fill="none" stroke="#e2b80e" stroke-width="1.6"/><path d="M6 9l2 2 4-4" fill="none" stroke="#e2b80e" stroke-width="1.6"/></svg>Commit to our customer's long-term success.</li>
  </ul>
  <div class="btn" style="left:60px;top:493px;width:133px;height:37px">Our Story</div>
</section>
<svg class="abs" style="left:0;top:600px" width="1200" height="80" viewBox="0 0 1200 80">
  <polygon points="0,8 560,60 0,78" fill="#24609a"/>
  <polygon points="0,78 1200,0 1200,80 0,80" fill="#f2f6fa"/>
</svg>

<!-- SERVICES -->
<section class="services"></section>
<h2 class="sec-title" style="left:61px;top:740px">Transformation <span class="accent">Supported by Technology</span></h2>
<div class="btn" style="left:984px;top:750px;width:156px;height:37px">How We Work</div>
<p class="lead">During our early years, Corvalin focused only on business transformation. We came to realize that successful transformation often depended on quality software implementations, and often more than one. Now we focus on five things, the five things most businesses need to reach their goals.</p>

<article class="card" style="left:60px">
  <div class="icon"><svg width="44" height="40" viewBox="0 0 44 40"><rect x="4" y="4" width="34" height="24" fill="none" stroke="#111" stroke-width="1.6"/><path d="M10 22v-5M16 22v-9M22 22v-6" stroke="#111" stroke-width="2"/><circle cx="32" cy="22" r="6" fill="none" stroke="#24609a" stroke-width="1.8"/><path d="M36 26l5 5" stroke="#24609a" stroke-width="2"/><path d="M14 28l-4 9M28 28l4 9" stroke="#111" stroke-width="1.6"/></svg></div>
  <h3>Business<br>Transformation</h3>
  <p>Define and execute your<br>strategy.</p>
  <div class="go"><svg width="18" height="14" viewBox="0 0 18 14"><path d="M1 7h15M10 1l6 6-6 6" fill="none" stroke="#fff" stroke-width="1.8"/></svg></div>
  <div class="media" role="img" aria-label="Photo of hands reviewing printed business charts beside a laptop" style="background:linear-gradient(135deg,#5f6670,#cfd8e3 55%,#7aa6d2)"></div>
</article>
<article class="card" style="left:335px">
  <div class="icon solid"><svg width="44" height="40" viewBox="0 0 44 40"><rect x="4" y="6" width="36" height="24" fill="none" stroke="#fff" stroke-width="1.6"/><path d="M12 24v-6M18 24v-10M24 24v-7M30 24v-12" stroke="#fff" stroke-width="2"/><circle cx="11" cy="12" r="4" fill="none" stroke="#fff" stroke-width="1.4"/><path d="M16 34h12" stroke="#fff" stroke-width="1.8"/></svg></div>
  <h3>ERP<br>Implementations</h3>
  <p>Assess, upgrade, and implement ERP solutions to meet your needs.</p>
  <div class="go hl"><svg width="18" height="14" viewBox="0 0 18 14"><path d="M1 7h15M10 1l6 6-6 6" fill="none" stroke="#111" stroke-width="1.8"/></svg></div>
  <div class="media" role="img" aria-label="Photo of a person typing on a laptop with floating interface panels" style="background:linear-gradient(135deg,#5a5e64,#a3a8ae 50%,#3f4349)"></div>
</article>
<article class="card" style="left:610px">
  <div class="icon"><svg width="44" height="40" viewBox="0 0 44 40"><rect x="4" y="6" width="36" height="28" rx="2" fill="none" stroke="#111" stroke-width="1.6"/><rect x="26" y="2" width="14" height="8" rx="1" fill="#fff" stroke="#24609a" stroke-width="1.4"/><circle cx="14" cy="20" r="5" fill="none" stroke="#111" stroke-width="1.6"/><path d="M24 16h12M24 21h12M24 26h10" stroke="#111" stroke-width="1.6"/></svg></div>
  <h3>CRM<br>Implementations</h3>
  <p>Take your relationships to the next level.</p>
  <div class="go"><svg width="18" height="14" viewBox="0 0 18 14"><path d="M1 7h15M10 1l6 6-6 6" fill="none" stroke="#fff" stroke-width="1.8"/></svg></div>
  <div class="media" role="img" aria-label="Digital illustration of a glowing customer network around a central hub" style="background:radial-gradient(circle at 55% 30%,#4fa9e0 0%,#1c3550 45%,#0c1420 100%)"></div>
</article>
<article class="card" style="left:885px">
  <div class="icon"><svg width="44" height="40" viewBox="0 0 44 40"><rect x="4" y="4" width="34" height="26" rx="2" fill="none" stroke="#111" stroke-width="1.6"/><circle cx="13" cy="15" r="5" fill="none" stroke="#111" stroke-width="1.6"/><path d="M22 20v-4M26 20v-7M30 20v-5" stroke="#111" stroke-width="2"/><circle cx="30" cy="28" r="5" fill="none" stroke="#24609a" stroke-width="1.8"/><path d="M34 32l5 5" stroke="#24609a" stroke-width="2"/></svg></div>
  <h3>BI and Data</h3>
  <p>Discover, connect, and trust your data.</p>
  <div class="go"><svg width="18" height="14" viewBox="0 0 18 14"><path d="M1 7h15M10 1l6 6-6 6" fill="none" stroke="#fff" stroke-width="1.8"/></svg></div>
  <div class="media" role="img" aria-label="Photo of a laptop showing data dashboards on a wooden desk" style="background:linear-gradient(160deg,#eef0f2,#c9ccd0 45%,#b88a5a 80%)"></div>
</article>
<div class="pager" style="left:567px;top:1311px"><i></i><i class="on"></i></div>

<!-- PEOPLE -->
<div class="ghost" style="left:14px">People</div>
<div class="ghost" style="left:998px">It’s the</div>
<h2 class="sec-title" style="left:0;top:1426px;width:1200px;text-align:center;font-size:50px">It’s the <span class="accent">People</span></h2>
<div class="people-band"></div>
<div class="ring"></div>
<div class="people-photo" role="img" aria-label="Photo of a team gathered around a laptop with a glowing digital overlay"></div>
<p class="people-copy" style="top:1520px">The world has changed in the past twenty years. The people you need might not all work for one company. Our clients want the best resources, available quickly. That’s why, in addition to our team of experts, we partner with:</p>
<ul class="people-list">
  <li style="top:1597px"><svg width="18" height="18" viewBox="0 0 18 18"><path d="M3 9a6 6 0 0 1 10.5-4M15 9a6 6 0 0 1-10.5 4" fill="none" stroke="#24609a" stroke-width="1.6"/><path d="M6 9l2 2 4-4" fill="none" stroke="#24609a" stroke-width="1.6"/></svg>A large network of expert consultants who are the best at what they do,</li>
  <li style="top:1628px"><svg width="18" height="18" viewBox="0 0 18 18"><path d="M3 9a6 6 0 0 1 10.5-4M15 9a6 6 0 0 1-10.5 4" fill="none" stroke="#24609a" stroke-width="1.6"/><path d="M6 9l2 2 4-4" fill="none" stroke="#24609a" stroke-width="1.6"/></svg>Service providers all over the world to provide the resources and value that are right for you, available 24 x 7.</li>
</ul>
<p class="people-copy" style="top:1686px">People are invariably at the center of our customer’s success. Find out how we can add our experts to yours.</p>
<div class="btn" style="left:550px;top:1760px;width:160px;height:37px">Meet Our Team</div>

<!-- TESTIMONIALS -->
<section class="reviews"><h2>What Our Client Are Says...</h2></section>
<div class="slide-btn" style="left:67px;background:var(--white)"><svg width="18" height="14" viewBox="0 0 18 14"><path d="M17 7H2M8 1L2 7l6 6" fill="none" stroke="#111" stroke-width="1.8"/></svg></div>
<div class="slide-btn" style="left:1081px;background:var(--yellow)"><svg width="18" height="14" viewBox="0 0 18 14"><path d="M1 7h15M10 1l6 6-6 6" fill="none" stroke="#111" stroke-width="1.8"/></svg></div>

<div class="quote" style="left:151px">
  <p>Lorem Ipsum is simply dummy text of the printing and typesetting industry. Lorem Ipsum has been the industry's standard dummy text ever since the 1500s, when an unknown printer took a galley of type and scrambled it to make a type specimen book. It has survived not only five centuries.</p>
  <div class="rating"><svg width="96" height="16" viewBox="0 0 96 16"><g fill="#e2b80e"><path id="st" d="M8 0l2.4 5 5.4.6-4 3.7 1.1 5.4L8 12 3.1 14.7l1.1-5.4-4-3.7L5.6 5z"/><use href="#st" x="20"/><use href="#st" x="40"/><use href="#st" x="60"/><use href="#st" x="80"/></g></svg><b>4.9 reviews</b></div>
  <div class="tail"></div>
</div>
<div class="quote" style="left:614px">
  <p>Lorem Ipsum is simply dummy text of the printing and typesetting industry. Lorem Ipsum has been the industry's standard dummy text ever since the 1500s, when an unknown printer took a galley of type and scrambled it to make a type specimen book. It has survived not only five centuries.</p>
  <div class="rating"><svg width="96" height="16" viewBox="0 0 96 16"><g fill="#e2b80e"><use href="#st"/><use href="#st" x="20"/><use href="#st" x="40"/><use href="#st" x="60"/><use href="#st" x="80"/></g></svg><b>4.9 reviews</b></div>
  <div class="tail"></div>
</div>
<div class="author" style="left:163px"><div class="avatar" role="img" aria-label="Portrait photo of the client"></div><div><div class="name">Martin Hale</div><div class="co">Company Name</div></div></div>
<div class="author" style="left:624px"><div class="avatar" role="img" aria-label="Portrait photo of the client" style="background:linear-gradient(160deg,#dfe5ea,#8fa1b2)"></div><div><div class="name">Martin Hale</div><div class="co">Company Name</div></div></div>

<!-- PARTNERS -->
<h2 class="partners-title">Transformation <span class="accent">Supported by Technology</span></h2>
<div class="tile" style="left:60px"><span class="sq"></span>Lumora</div>
<div class="tile active" style="left:279px">Seekly</div>
<div class="tile" style="left:498px">Verano</div>
<div class="tile" style="left:717px">Notiva</div>
<div class="tile" style="left:936px"><span class="sq"></span>Cellix</div>
<div class="pager" style="left:517px;top:2795px"><i></i><i class="on"></i><i></i><i></i><i></i></div>

<!-- FOOTER -->
<svg class="footer-shape" width="1200" height="70" viewBox="0 0 1200 70">
  <polygon points="840,84 1200,3 1200,65" fill="#e2b80e"/>
  <polygon points="0,84 1200,65 1200,70 0,70" fill="#2b3547"/>
</svg>
<footer class="footer"></footer>
<div class="logo" style="left:60px;top:2966px;font-size:46px;color:var(--white)"><span class="mark"></span>Corvalin</div>
<p class="f-about">Lorem Ipsum is simply dummy text of the printing and typesetting industry. Lorem Ipsum has been the industry's.</p>
<div class="f-col"><h4 style="left:339px">Quick Links:</h4><h4 style="left:614px">Contact Us:</h4><h4 style="left:890px">Connect With Us:</h4></div>
<div class="f-link" style="top:3016px">About Us</div>
<div class="f-link" style="top:3048px">Services</div>
<div class="f-link" style="top:3079px">Insights</div>
<div class="f-link" style="top:3110px">Join Us</div>
<div class="f-link" style="top:3141px">Contact Us</div>
<div class="f-contact" style="top:3012px;width:230px"><svg width="16" height="18" viewBox="0 0 16 18"><path d="M8 1a5 5 0 0 1 5 5c0 4-5 9-5 9S3 10 3 6a5 5 0 0 1 5-5z" fill="none" stroke="#e2b80e" stroke-width="1.6"/><circle cx="8" cy="6" r="1.8" fill="#e2b80e"/></svg>123, Lorem Ipsum is simply dummy text of the printing.</div>
<div class="f-contact" style="top:3063px;font-weight:600"><svg width="16" height="16" viewBox="0 0 16 16"><path d="M3 1l3 3-2 2a9 9 0 0 0 6 6l2-2 3 3-2 2C7 15 1 9 1 3z" fill="none" stroke="#e2b80e" stroke-width="1.5"/></svg>123 456 7890</div>
<div class="f-contact" style="top:3096px"><svg width="18" height="13" viewBox="0 0 18 13"><rect x="1" y="1" width="16" height="11" fill="none" stroke="#e2b80e" stroke-width="1.5"/><path d="M1 1l8 6 8-6" fill="none" stroke="#e2b80e" stroke-width="1.5"/></svg>info@corvalin.com</div>
<div class="social" style="left:888px"></div>
<div class="social" style="left:927px"></div>
<div class="social on" style="left:967px"></div>
<div class="social" style="left:1007px"></div>
<div class="copyright">© 2023 Copyright. Corvalin. All Right Reserved.</div>

</body>
</html>
```